Bubble map/flip book

I need someone to create a bubble map with explanations using the attached. This will be used to create a color coded flip book/manual. I need you to clean this up.

Dorothywinslade@postlark.com

```html
<!DOCTYPE html>
<html lang="en">
<head>
<meta charset="utf-8">
<title>Claim Has Denied – Bubble Map</title>
<link rel="stylesheet" href="https://fonts.googleapis.com/css2?family=Montserrat:wght@700&family=Staatliches&display=swap">
<style>
  :root {
    --bg: #ffffff;
    --hub: #0657a3;
    --ink: #ffffff;
    --auth: #a88a10;
    --coding: #f00000;
    --duplicate: #0d5a0a;
    --wow: #474542;
    --global: #5a18c8;
    --info: #0a14f0;
    --timely: #e07a0a;
  }
  html, body {
    margin: 0;
    padding: 0;
    width: 1200px;
    height: 848px;
    overflow: hidden;
    background: var(--bg);
  }
  .bubble-map { display: block; width: 1200px; height: 848px; }
  .connector { fill: none; stroke-width: 4; }
  .hub { fill: var(--hub); }
  .stamp-frame { fill: none; stroke: var(--ink); }
  .stamp-text {
    font-family: "Staatliches", "Impact", sans-serif;
    fill: var(--ink);
    text-anchor: middle;
  }
  .node-label {
    font-family: "Montserrat", "Arial", sans-serif;
    font-weight: 700;
    font-size: 18px;
    fill: var(--ink);
    text-anchor: middle;
  }
  .icon { fill: var(--ink); }
  .icon-line { fill: none; stroke: var(--ink); stroke-width: 4; stroke-linecap: round; stroke-linejoin: round; }
  .auth { fill: var(--auth); } .auth-stroke { stroke: var(--auth); }
  .coding { fill: var(--coding); } .coding-stroke { stroke: var(--coding); }
  .duplicate { fill: var(--duplicate); } .duplicate-stroke { stroke: var(--duplicate); }
  .wow { fill: var(--wow); } .wow-stroke { stroke: var(--wow); }
  .global { fill: var(--global); } .global-stroke { stroke: var(--global); }
  .info { fill: var(--info); } .info-stroke { stroke: var(--info); }
  .timely { fill: var(--timely); } .timely-stroke { stroke: var(--timely); }
</style>
</head>
<body>
<svg class="bubble-map" viewBox="0 0 1200 848" xmlns="http://www.w3.org/2000/svg">
  <!-- connectors -->
  <g class="connectors">
    <path class="connector auth-stroke" d="M312,230 C150,230 122,262 124,462"/>
    <path class="connector coding-stroke" d="M346,306 C282,326 266,380 266,460 L266,630"/>
    <path class="connector duplicate-stroke" d="M428,360 L428,462"/>
    <path class="connector wow-stroke" d="M594,400 L594,640"/>
    <path class="connector global-stroke" d="M756,380 L756,462"/>
    <path class="connector info-stroke" d="M896,306 C930,326 934,380 932,460 L928,630"/>
    <path class="connector timely-stroke" d="M932,226 C1058,226 1084,280 1084,462"/>
  </g>

  <!-- hub -->
  <g class="hub-node">
    <ellipse class="hub" cx="622" cy="220" rx="310" ry="186"/>
    <g class="stamp" transform="rotate(-6 624 220)">
      <rect class="stamp-frame" x="392" y="96" width="464" height="252" rx="14" stroke-width="7"/>
      <rect class="stamp-frame" x="406" y="110" width="436" height="224" rx="8" stroke-width="3"/>
      <text class="stamp-text" x="624" y="196" font-size="96" letter-spacing="4">CLAIM HAS</text>
      <text class="stamp-text" x="624" y="316" font-size="150" letter-spacing="6">DENIED</text>
    </g>
  </g>

  <!-- Auth referral -->
  <g class="node">
    <ellipse class="auth" cx="124" cy="546" rx="112" ry="84"/>
    <circle class="icon" cx="98" cy="500" r="16"/>
    <path class="icon" d="M66,552 C66,524 130,524 130,552 Z"/>
    <circle class="icon" cx="136" cy="514" r="16" stroke="var(--auth)" stroke-width="4"/>
    <path class="icon" d="M104,568 C104,536 170,536 170,568 Z" stroke="var(--auth)" stroke-width="4"/>
    <path class="icon-line" d="M128,476 C160,470 180,500 172,532" stroke-width="3"/>
    <path class="icon-line" d="M134,468 L124,478 L136,486" stroke-width="3"/>
    <text class="node-label" x="126" y="594">AUTH REFERAL</text>
    <text class="node-label" x="126" y="613">NEEDED</text>
  </g>

  <!-- Coding / billing -->
  <g class="node">
    <ellipse class="coding" cx="270" cy="712" rx="112" ry="84"/>
    <text class="node-label" x="222" y="692" font-size="26">&lt;/&gt;</text>
    <path class="icon-line" d="M262,642 L310,642 L326,658 L326,732 L262,732 Z"/>
    <path class="icon-line" d="M276,660 L312,660 M276,676 L312,676 M276,692 L312,692 M276,708 L296,708" stroke-width="5"/>
    <text class="node-label" x="306" y="724" font-size="18">$</text>
    <text class="node-label" x="270" y="760">CODING / BILLING</text>
    <text class="node-label" x="270" y="779">ISSUES</text>
  </g>

  <!-- Duplicate -->
  <g class="node">
    <ellipse class="duplicate" cx="428" cy="546" rx="112" ry="84"/>
    <path class="icon-line" d="M372,480 L414,476 L420,562 L380,566 Z" stroke-width="3"/>
    <path class="icon-line" d="M382,492 L410,490 M383,504 L411,502 M384,516 L412,514 M385,528 L413,526 M386,540 L414,538" stroke-width="3"/>
    <path class="icon" d="M410,482 L454,482 L472,500 L472,580 L410,580 Z"/>
    <path class="icon-line" d="M420,500 L458,500 M420,512 L462,512 M420,524 L462,524 M420,536 L462,536 M420,548 L462,548 M420,560 L462,560" stroke="var(--duplicate)" stroke-width="3"/>
    <text class="node-label" x="430" y="602">DUPLICATE</text>
  </g>

  <!-- Wow coverage charge -->
  <g class="node">
    <ellipse class="wow" cx="594" cy="722" rx="112" ry="84"/>
    <circle class="icon" cx="542" cy="702" r="20"/>
    <text class="node-label" x="542" y="711" font-size="24" fill="var(--wow)" style="fill:var(--wow)">$</text>
    <path class="icon" d="M572,690 L584,668 L598,680 L612,660 L622,676 L640,664 L636,684 L664,690 L640,700 L650,716 L624,712 L612,730 L600,714 L576,722 L586,704 Z"/>
    <text class="node-label" x="612" y="704" font-size="20" style="fill:var(--wow)">wow!</text>
    <text class="node-label" x="596" y="768">WOW COVERAGE</text>
    <text class="node-label" x="596" y="787">CHARGE</text>
  </g>

  <!-- Global inclusive -->
  <g class="node">
    <ellipse class="global" cx="756" cy="546" rx="112" ry="84"/>
    <circle class="icon-line" cx="758" cy="516" r="44" stroke-width="4"/>
    <ellipse class="icon-line" cx="758" cy="516" rx="18" ry="44" stroke-width="3"/>
    <path class="icon-line" d="M758,472 L758,560 M716,500 L800,500 M716,532 L800,532" stroke-width="3"/>
    <rect class="icon" x="676" y="506" width="90" height="20"/>
    <path class="icon-line" d="M684,516 L760,516 M750,508 L760,516 L750,524" stroke="var(--global)" stroke-width="3"/>
    <text class="node-label" x="758" y="590">GLOBAL</text>
    <text class="node-label" x="758" y="609">INCLUSIVE</text>
  </g>

  <!-- Additional information -->
  <g class="node">
    <ellipse class="info" cx="926" cy="712" rx="112" ry="84"/>
    <circle class="icon" cx="884" cy="688" r="18"/>
    <path class="icon-line" d="M884,678 L884,698 M874,688 L894,688" stroke="var(--info)" stroke-width="5"/>
    <circle class="icon-line" cx="940" cy="666" r="32" stroke-width="5"/>
    <text class="node-label" x="940" y="686" font-size="46" font-style="italic" style="font-family:Georgia,serif">i</text>
    <text class="node-label" x="928" y="736">ADDITIONAL</text>
    <text class="node-label" x="928" y="755">INFORMATION</text>
    <text class="node-label" x="928" y="774">REQUESTED</text>
  </g>

  <!-- Past timely filing -->
  <g class="node">
    <ellipse class="timely" cx="1072" cy="546" rx="112" ry="84"/>
    <path class="icon" d="M1002,490 L1040,478 L1058,492 L1068,560 L1018,574 Z" transform="rotate(-4 1030 530)"/>
    <path class="icon-line" d="M1016,504 L1046,496 M1018,516 L1050,508 M1020,528 L1052,520 M1022,540 L1054,532 M1024,552 L1046,546" stroke="var(--timely)" stroke-width="3"/>
    <circle cx="1106" cy="528" r="30" fill="var(--timely)" stroke="var(--ink)" stroke-width="5"/>
    <path class="icon-line" d="M1100,540 L1110,524 L1122,524"/>
    <text class="node-label" x="1076" y="594">PAST TIMELY</text>
    <text class="node-label" x="1076" y="613">FILING</text>
  </g>
</svg>
</body>
</html>
```